M Website

We need a website design for a construction plant company. You may use a combination of our photos and the stock images. See the logo for company colours. It also be of great value to see moving pictures like the ones on the link: https://www.bellwickventures.co.za/copy-of-about-us. See our uploaded files for content.

Target Market(s)

Construction

Number of Pages Required

5+ page

```html
<!DOCTYPE html>
<html lang="en">
<head>
<meta charset="utf-8">
<title>Tarrow Logistics – Construction Projects</title>
<link href="https://fonts.googleapis.com/css2?family=Montserrat:wght@600;700;800&family=Open+Sans:wght@400;600;700&display=swap" rel="stylesheet">
<style>
:root{
  --yellow:#f7c016;
  --yellow-deep:#e8ae00;
  --dark:#1b1b1b;
  --footer:#161616;
  --ink:#111;
  --text:#555;
  --muted:#888;
  --line:#d8d8d8;
  --soft:#efefef;
  --white:#fff;
}
*{box-sizing:border-box;margin:0;padding:0}
html,body{width:1200px;height:4467px;overflow:hidden}
body{position:relative;background:var(--white);font-family:"Open Sans",Arial,sans-serif;color:var(--text)}
.abs{position:absolute}
h1,h2,h3,h4,.brand{font-family:"Montserrat",Arial,sans-serif}

/* header */
.site-header{left:0;top:0;width:1200px;height:115px;background:var(--dark)}
.brand{left:112px;top:22px;display:flex;align-items:center;gap:10px;color:var(--yellow);font-weight:800;font-size:30px;letter-spacing:1px}
.brand .dot{width:34px;height:34px;border-radius:50%;background:var(--yellow)}
.main-nav{right:112px;top:46px;display:flex;gap:32px;font-family:"Montserrat",Arial,sans-serif;font-weight:700;font-size:15px;color:var(--white)}
.main-nav a{color:inherit;text-decoration:none;position:relative}
.main-nav a.active::before{content:"";position:absolute;left:50%;top:50%;width:40px;height:40px;transform:translate(-50%,-50%);border-radius:50%;border:1px solid var(--yellow);border-left-color:transparent;border-bottom-color:transparent}

/* hero */
.hero{left:0;top:115px;width:1200px;height:720px}
.hero-photo{position:absolute;inset:0;background:linear-gradient(180deg,#6f7983 0%,#b49a6e 35%,#c8914a 60%,#a87236 100%)}
.hero-title{left:0;width:1200px;top:300px;text-align:center;color:var(--white);font-weight:800;font-size:76px;letter-spacing:3px;text-shadow:0 2px 8px rgba(0,0,0,.35)}
.hero-sub{left:0;width:1200px;top:408px;text-align:center;color:var(--white);font-family:"Montserrat",Arial,sans-serif;font-weight:600;font-size:30px}
.play{left:563px;top:205px;width:74px;height:74px;border:3px solid var(--white);border-radius:50%}
.play::after{content:"";position:absolute;left:26px;top:19px;border-left:24px solid var(--white);border-top:15px solid transparent;border-bottom:15px solid transparent}
.mouse{left:582px;top:528px;width:36px;height:56px;border:3px solid var(--white);border-radius:18px}
.mouse::after{content:"";position:absolute;left:14px;top:9px;width:3px;height:12px;background:var(--white);border-radius:2px}
.chev{left:587px;top:590px}

/* section headings */
.heading-line{font-weight:800;font-size:52px;color:var(--ink);letter-spacing:1px;display:flex;align-items:center;gap:22px}
.heading-line::after{content:"";width:110px;height:5px;background:var(--yellow)}
.heading-center{left:0;width:1200px;text-align:center;font-weight:800;font-size:52px;color:var(--ink);letter-spacing:1px}

/* about */
.about-title{left:112px;top:945px}
.about-text{left:112px;top:1038px;width:460px;font-size:14.5px;line-height:25px}
.about-text p+p{margin-top:26px}
.btn{display:inline-block;background:var(--yellow);color:var(--ink);font-family:"Montserrat",Arial,sans-serif;font-weight:700;font-size:14px;border-radius:24px;padding:15px 30px;text-transform:uppercase}
.about-btn{left:112px;top:1283px}
.about-art{left:560px;top:920px;width:640px;height:420px}
.about-photo{left:628px;top:958px;width:442px;height:330px;border-radius:50% 50% 42% 46% / 56% 54% 46% 44%;background:linear-gradient(170deg,#c89a57 0%,#d6a24a 45%,#8a6a3b 100%)}
.divider{left:112px;top:1443px;width:976px;height:1px;background:var(--line)}

/* services */
.services-title{top:1535px}
.services-intro{left:300px;width:600px;top:1628px;text-align:center;font-size:14.5px;line-height:26px}
.service{top:1728px;width:392px;height:282px}
.service .img{position:absolute;inset:0}
.service h3{position:absolute;left:0;right:0;bottom:30px;text-align:center;color:var(--white);font-size:28px;font-weight:700;text-shadow:0 2px 6px rgba(0,0,0,.6)}

/* team */
.team-title{left:112px;top:2130px}
.member{top:2243px;width:225px;height:275px;background:var(--white);border:1px solid #e6e6e6}
.member.featured{height:308px;box-shadow:0 4px 14px rgba(0,0,0,.18)}
.member .photo{height:182px;background:linear-gradient(180deg,#cfd3d7,#8c939b)}
.member h4{margin:22px 15px 0;font-size:16px;font-weight:700;color:var(--ink)}
.member .rule{margin:8px 15px 0;width:110px;height:1px;background:var(--line)}
.member .who{margin:12px 15px 0;font-size:12px;color:var(--muted)}
.member .socials{margin:14px 15px 0;display:flex;gap:8px}
.member .socials span{width:10px;height:10px;border-radius:50%;background:#3b5998}
.pager{left:112px;top:2586px;width:220px;text-align:center;font-size:18px;color:var(--ink)}
.pager b{color:var(--yellow)}
.pager-line{left:112px;top:2614px;width:860px;height:2px;background:#ddd}
.pager-line::before{content:"";position:absolute;left:0;top:0;width:220px;height:2px;background:var(--ink)}

/* testimonials */
.testi-bg{left:0;top:2640px;width:1200px;height:525px;background:var(--soft)}
.testi-title{top:2723px}
.quote{top:2850px;width:340px;height:215px;padding:56px 20px 0}
.quote.featured{background:var(--white);border:1px solid #ddd;box-shadow:0 3px 10px rgba(0,0,0,.08)}
.quote .mark{position:absolute;left:0;top:0;width:40px;height:40px;border-radius:50%;background:var(--yellow);color:var(--white);font-family:Georgia,serif;font-weight:700;font-size:38px;line-height:50px;text-align:center}
.quote.featured .mark{left:20px;top:-20px}
.quote p{font-style:italic;font-size:13.5px;line-height:23px;color:#666}
.quote .by{margin-top:16px;font-size:13px;color:var(--muted)}
.quote .by b{color:var(--ink)}
.arrow{top:2940px;font-size:40px;color:#222;font-family:"Montserrat",Arial,sans-serif}

/* partners */
.partners-title{top:3140px}
.partners-sub{left:0;width:1200px;top:3218px;text-align:center;font-size:13px;font-style:italic;color:var(--muted)}
.partner{top:3295px;width:180px;height:84px;border-radius:42px;background:var(--white);border:1px solid #e2e2e2;box-shadow:0 2px 8px rgba(0,0,0,.06)}
.partner i{position:absolute;left:60px;top:20px;width:60px;height:44px;border-radius:6px;background:#cfcfcf}

/* features */
.feature-band{left:0;top:3470px;width:1200px;height:590px}
.features-title{top:3590px;color:var(--white)}
.feature{width:225px;color:var(--white)}
.feature .icon{width:88px;height:80px;border-radius:12px;border:3px solid var(--ink)}
.feature h4{margin-top:24px;font-size:20px;font-weight:700;letter-spacing:1px}
.feature p{margin-top:12px;font-size:13.5px;line-height:23px}
.quote-btn{left:500px;top:3912px;width:200px;text-align:center;background:var(--ink);color:var(--white)}

/* footer */
.site-footer{left:0;top:4055px;width:1200px;height:412px;background:var(--footer);color:#cfcfcf}
.foot-brand{left:140px;top:4160px;display:flex;align-items:center;gap:10px;color:var(--yellow);font-weight:800;font-size:30px}
.foot-brand .dot{width:36px;height:36px;border-radius:50%;background:var(--yellow)}
.foot-social{left:118px;top:4295px;display:flex;gap:14px}
.foot-social span{width:18px;height:18px;border-radius:50%;background:#e9e9e9}
.foot-col{color:#d8d8d8}
.foot-col h4{font-size:16px;font-weight:700;color:var(--white);letter-spacing:.5px}
.foot-links{margin-top:22px;list-style:none;font-size:13px;line-height:24px}
.foot-links li::before{content:"▸ ";color:#aaa}
.contact-row{display:flex;gap:14px;margin-top:20px;font-size:13px;line-height:20px}
.contact-row svg{flex:none;margin-top:2px}
.news p{margin-top:20px;font-size:13px;line-height:20px;width:260px}
.email-field{margin-top:12px;width:255px;height:34px;border:1px solid #888;font-size:12px;padding:8px 10px;color:#ccc}
.sub-btn{margin-top:14px;display:inline-block;background:var(--yellow);color:var(--ink);border-radius:16px;padding:7px 18px;font-size:11px;font-weight:700;text-transform:uppercase;font-family:"Montserrat",Arial,sans-serif}
.copyright{left:0;width:1200px;top:4415px;text-align:center;font-size:13px;color:#ddd}
</style>
</head>
<body>

<header class="site-header abs">
  <div class="brand abs"><span class="dot"></span>TARROW</div>
  <nav class="main-nav abs">
    <a class="active" href="#">HOME</a><a href="#">ABOUT US</a><a href="#">OUR MISSION</a><a href="#">PROJECTS</a><a href="#">BLOG</a><a href="#">CONTACT</a>
  </nav>
</header>

<section class="hero abs">
  <div class="hero-photo" role="img" aria-label="Excavator and grader working on a gravel construction site at sunset"></div>
  <svg class="abs" style="left:0;top:540px" width="1200" height="180" viewBox="0 0 1200 180">
    <path d="M0 30 Q600 250 1200 30 L1200 180 L0 180Z" fill="#fff"/>
    <path d="M0 30 Q600 250 1200 30" fill="none" stroke="#f7c016" stroke-width="12"/>
  </svg>
  <div class="play abs"></div>
  <h1 class="hero-title abs">TARROW LOGISTICS</h1>
  <div class="hero-sub abs">Construction Projects</div>
  <div class="mouse abs"></div>
  <svg class="chev abs" width="26" height="26" viewBox="0 0 26 26"><path d="M3 3l10 9 10-9M3 13l10 9 10-9" fill="none" stroke="#fff" stroke-width="3"/></svg>
</section>

<section class="about">
  <h2 class="heading-line about-title abs">ABOUT US</h2>
  <div class="about-text abs">
    <p>Tarrow Logistics and Plant Hire (Pty) Ltd is a Black Woman owned Construction and Plant Hire company operating mainly from the head office in Ashvale (Kestrel North). Tarrow Logistics and Plant Hire (Pty) Ltd was established in 2014, and has worked in various municipal jurisdictions within South Africa.</p>
    <p>Tarrow Logistics and Plant Hire (Pty) Ltd has expertise in the following key fields and has successfully executed projects in most of them.</p>
  </div>
  <span class="btn about-btn abs">Read more ➜</span>
  <svg class="about-art abs" width="640" height="420" viewBox="0 0 640 420">
    <circle cx="430" cy="120" r="125" fill="#f7c016"/>
    <path d="M12 410 Q30 330 120 320 Q80 370 110 400 Z" fill="#cfcfcf"/>
    <path d="M520 310 Q610 330 620 410 Q560 380 500 360 Z" fill="#cfcfcf"/>
  </svg>
  <div class="about-photo abs" role="img" aria-label="Yellow motor grader on a construction site"></div>
  <div class="divider abs"></div>
</section>

<section class="services">
  <h2 class="heading-center services-title abs">SERVICES</h2>
  <p class="services-intro abs">Tarrow Logistics and Plant Hire (Pty) Ltd has expertise in the following key fields and has successfully executed projects in most of them.</p>
  <div class="service abs" style="left:6px"><div class="img" role="img" aria-label="Road roller laying fresh asphalt" style="background:linear-gradient(180deg,#7d8c95,#3f4a52 55%,#23282c)"></div><h3>Roads &amp; Stormwater</h3></div>
  <div class="service abs" style="left:404px"><div class="img" role="img" aria-label="Blue water pipe laid in a dug trench" style="background:linear-gradient(90deg,#7a5030,#4d6f8f 48%,#7a5030)"></div><h3>Water Infrastructure</h3></div>
  <div class="service abs" style="left:802px"><div class="img" role="img" aria-label="Workers paving a housing estate road" style="background:linear-gradient(180deg,#9fb2c2,#6b6c64 45%,#2a2a2a)"></div><h3>Sanitation &amp; Housing</h3></div>
</section>

<section class="team">
  <h2 class="heading-line team-title abs">OUR TEAM</h2>
  <div class="member featured abs" style="left:112px"><div class="photo" role="img" aria-label="Portrait of the managing director"></div><h4>Managing Director</h4><div class="rule"></div><div class="who">Lerato Moyo</div><div class="socials"><span></span><span style="background:#1da1f2"></span><span style="background:#0077b5"></span></div></div>
  <div class="member abs" style="left:362px"><div class="photo" role="img" aria-label="Portrait of the general manager"></div><h4>General Manager</h4><div class="rule"></div><div class="who">Thabo Nkosi</div></div>
  <div class="member abs" style="left:612px"><div class="photo" role="img" aria-label="Portrait of the financial officer"></div><h4>Financial Officer</h4><div class="rule"></div><div class="who">Anna Botha</div></div>
  <div class="member abs" style="left:862px"><div class="photo" role="img" aria-label="Portrait of the contracts manager"></div><h4>Contracts Manager</h4><div class="rule"></div><div class="who">Sipho Dlamini</div></div>
  <div class="member abs" style="left:1112px"><div class="photo" role="img" aria-label="Portrait of the safety officer"></div><h4>Safety Officer</h4><div class="rule"></div><div class="who">Karin Smit</div></div>
  <div class="pager abs"><b>‹</b> 1 / 8 <b>›</b></div>
  <div class="pager-line abs"></div>
</section>

<section class="testimonials">
  <div class="testi-bg abs">
    <svg width="1200" height="525" viewBox="0 0 1200 525"><ellipse cx="60" cy="260" rx="330" ry="230" fill="#fff"/><ellipse cx="1140" cy="260" rx="330" ry="230" fill="#fff"/></svg>
  </div>
  <h2 class="heading-center testi-title abs">TESTIMONIALS</h2>
  <div class="arrow abs" style="left:28px">‹</div>
  <div class="arrow abs" style="left:1148px">›</div>
  <div class="quote abs" style="left:95px"><span class="mark">“</span><p>Lorem ipsum dolor sit amet, consectetur adipiscing elit, sed do eiusmod tempor incidi dunt ut labore et dolore magna aliqua. Ut enim ad minim veniam... ”</p><div class="by">👤 <b>Sam Reyes</b>, Creative Manager.</div></div>
  <div class="quote featured abs" style="left:430px"><span class="mark">“</span><p>Lorem ipsum dolor sit amet, consectetur adipiscing elit, sed do eiusmod tempor incidi dunt ut labore et dolore magna aliqua. Ut enim ad minim veniam... ”</p><div class="by">👤 <b>Lena Park</b>, Creative Manager.</div></div>
  <div class="quote abs" style="left:790px"><span class="mark">“</span><p>Lorem ipsum dolor sit amet, consectetur adipiscing elit, sed do eiusmod tempor incidi dunt ut labore et dolore magna aliqua. Ut enim ad minim veniam... ”</p><div class="by">👤 <b>Omar Vale</b>, Creative Manager.</div></div>
</section>

<section class="partners">
  <h2 class="heading-center partners-title abs">OUR PARTNERS</h2>
  <p class="partners-sub abs">Some Of Our Recent Clients &amp; Partners</p>
  <div class="partner abs" style="left:112px"><i></i></div>
  <div class="partner abs" style="left:310px"><i></i></div>
  <div class="partner abs" style="left:510px"><i></i></div>
  <div class="partner abs" style="left:710px"><i></i></div>
  <div class="partner abs" style="left:908px"><i></i></div>
</section>

<section class="features">
  <svg class="feature-band abs" width="1200" height="590" viewBox="0 0 1200 590" role="img" aria-label="Yellow band over faded construction machinery">
    <defs><linearGradient id="band" x1="0" y1="0" x2="0" y2="1"><stop offset="0" stop-color="#f7c016"/><stop offset="1" stop-color="#e0a800"/></linearGradient></defs>
    <path d="M0 110 Q600 -60 1200 110 L1200 590 L0 590Z" fill="url(#band)"/>
    <path d="M0 110 Q600 -60 1200 110" fill="none" stroke="#1b1b1b" stroke-width="14"/>
  </svg>
  <h2 class="heading-center features-title abs">OUR FEATURE</h2>
  <div class="feature abs" style="left:112px;top:3680px"><div class="icon"></div><h4>INTEGRITY</h4><p>Maintaining the highest standards of quality.</p></div>
  <div class="feature abs" style="left:384px;top:3680px"><div class="icon"></div><h4>RELIABILITY</h4><p>Fulfilling the needs of our Clients.</p></div>
  <div class="feature abs" style="left:598px;top:3680px"><div class="icon"></div><h4>CAPABILITY</h4><p>Affording our staff personal growth through continuing...</p></div>
  <div class="feature abs" style="left:864px;top:3680px"><div class="icon"></div><h4>ETHICS</h4><p>Providing equal opportunity to all, in line with Government...</p></div>
  <span class="btn quote-btn abs">Get a quote ➜</span>
</section>

<footer class="site-footer abs"></footer>
<div class="foot-brand abs"><span class="dot"></span>TARROW</div>
<div class="foot-social abs"><span></span><span></span><span></span><span></span><span></span><span></span></div>
<div class="foot-col abs" style="left:390px;top:4150px">
  <h4>QUICK LINKS</h4>
  <ul class="foot-links"><li>Home</li><li>About Us</li><li>Services</li><li>Blog</li><li>Features</li><li>Contact Us</li></ul>
</div>
<div class="foot-col abs" style="left:580px;top:4150px">
  <h4>CONTACT US</h4>
  <div class="contact-row"><svg width="14" height="18" viewBox="0 0 14 18"><path d="M7 0a7 7 0 0 0-7 7c0 5 7 11 7 11s7-6 7-11a7 7 0 0 0-7-7zm0 9.5A2.5 2.5 0 1 1 7 4.5a2.5 2.5 0 0 1 0 5z" fill="#ddd"/></svg><span>Unit 4, Ridgeview Park<br>Kestrel 9410</span></div>
  <div class="contact-row"><svg width="14" height="14" viewBox="0 0 14 14"><path d="M3 0l3 3-2 2a8 8 0 0 0 5 5l2-2 3 3-2 3C6 14 0 8 0 2z" fill="#ddd"/></svg><span>+27 (0) 11 555 0142</span></div>
  <div class="contact-row"><svg width="16" height="12" viewBox="0 0 16 12"><rect width="16" height="12" rx="1" fill="#ddd"/><path d="M0 1l8 6 8-6" fill="none" stroke="#161616" stroke-width="1.5"/></svg><span>info@tarrowlogistics.co.za</span></div>
</div>
<div class="foot-col news abs" style="left:832px;top:4150px">
  <h4>NEWSLETTER SUBSCRIPTION</h4>
  <p>Register your Email Address to get More Information about us</p>
  <div class="email-field">Email Address</div>
  <span class="sub-btn">Subscribe</span>
</div>
<p class="copyright abs">Copyright © 2019 Tarrow Logistics. All Rights Reserved &nbsp;&nbsp;|&nbsp;&nbsp; Privacy Policy.</p>

</body>
</html>
```